依頼詳細
基本的な掲載コンテンツは変更はありません。コンテンツ間の連続性ある個別ページと各コンテンツへのゲートとなるトップページの2ページのデザインを希望いたします。
サイトURL
http://www.kusabe.or.jp/
ページ数
2ページ
希望イメージ
シンプル 複雑
単色 カラフル
暗い 明るい
日常 高級
遊び心 厳粛
未来的 伝統的
女性的 男性的
希望する色
緑・黄・赤
納品ファイル
• イラストレーター形式 (.ai)
• フォトショップ形式 (.psd)
• PNG形式 (.png)
補足説明
CMSはXoopsで構築いたしております。
ご提案いただきました皆様、本当にありがとうございます。

お寄せいただいた提案につきましては、関係者参集の上しっかり検討の上ご連絡差し上げたく存じます。今しばらくお待ちくださいませ。

まずはお礼まで。
■ 選んだ理由

当選案は今回多くの方から頂いた膨大なコンテンツで迷子になるというご指摘に対して、2名だけ下部にサイトマップ型のテキストナビゲーションで配慮された点に大きなポイントがありました。また言葉による説明だけではなく図解をプラスされていた点やデザインの再提出への応対スピード、さらなる修正にもドンドン応じるというメッセージに本気度の高さが見えてしまった点などは不利が有利に転じたポイントでもありました。本当に決定的な差がなく、プラスアルファに成否があったことは選考側にとってはうれしい悲鳴でしたが難航でした。

■ 提案者全員のお礼・コメント

まずは皆様、この度はご提案頂き大変ありがとうございました。どのご提案もよく配慮されており、現状のサイトの問題点を的確にご指摘いただいていました。選考委員が変われば結果も違ったと思うほどどの提案も素晴らしかったです。システムサイドからの視点、ユーザーサイドからの視点、発信者サイドからの視点それぞれの切り口からのご提案はとても興味深くたいへん勉強になりました。今回はご縁がございませんでした方も是非また機会がございましたらご提案くださいますよう、今後ともよろしくお願いいたします。

```html
<!DOCTYPE html>
<html lang="ja">
<head>
<meta charset="utf-8">
<title>さとやま便 | 地域情報ポータルサイト</title>
<link rel="stylesheet" href="https://fonts.googleapis.com/css2?family=Noto+Sans+JP:wght@400;500;700;900&display=swap">
<style>
:root{
  --green:#5aa62c;
  --green-dark:#3f7f1c;
  --green-light:#8cc94e;
  --green-pale:#e7f2d9;
  --leaf:#6fb536;
  --sky-top:#a9d9ef;
  --sky-bottom:#e4f4fa;
  --orange:#f08a1c;
  --red:#e43a2a;
  --text:#444;
  --muted:#888;
  --line:#d9d9d9;
  --placeholder:#d6d6d6;
  --page-bg:#eef5e4;
  --white:#fff;
}
*{box-sizing:border-box;margin:0;padding:0}
html,body{width:1200px;height:2492px;overflow:hidden}
body{font-family:"Noto Sans JP",sans-serif;color:var(--text);background:var(--page-bg);font-size:12px;position:relative}
a{color:inherit;text-decoration:none}
.abs{position:absolute}

/* header */
.sky{left:0;top:0;width:1200px;height:240px;background:linear-gradient(var(--sky-top),var(--sky-bottom))}
.cloud{background:rgba(255,255,255,.75);border-radius:50%}
.utility{left:0;top:0;width:1200px;height:26px;background:var(--white);border-bottom:2px solid var(--green);display:flex;justify-content:flex-end;align-items:center;padding-right:60px;gap:14px;font-size:11px;color:var(--green-dark)}
.tagline{left:78px;top:40px;font-size:11px;color:var(--green-dark);font-weight:500}
.site-name{left:74px;top:58px;display:flex;align-items:center;gap:10px}
.site-name .mark{width:20px;height:20px;border-radius:50%;background:var(--orange)}
.site-name strong{font-weight:700;font-size:44px;color:var(--green);letter-spacing:3px;line-height:1}
.site-sub{left:230px;top:112px;font-size:12px;color:var(--green);font-weight:700;letter-spacing:1px}
.font-size{left:684px;top:60px;display:flex;align-items:center;gap:4px;font-size:11px}
.font-size span.btn{width:22px;height:22px;border-radius:4px;background:var(--white);border:1px solid var(--line);display:flex;align-items:center;justify-content:center}
.font-size span.on{background:var(--green);color:var(--white);border-color:var(--green)}
.post-buttons{left:586px;top:110px;display:flex;gap:12px}
.post-btn{height:40px;padding:0 18px 0 10px;border-radius:6px;background:var(--green);color:var(--white);font-weight:700;font-size:15px;display:flex;align-items:center;gap:8px;box-shadow:0 3px 0 var(--green-dark)}
.post-btn i{width:22px;height:22px;border-radius:50%;background:var(--white);display:block}

/* main column */
.sheet{left:60px;top:172px;width:1080px;height:2122px;background:var(--white);box-shadow:0 0 6px rgba(0,0,0,.08)}
.slider{left:80px;top:186px;width:740px;height:314px;background:var(--placeholder);border:6px solid #eee}
.dots{left:700px;top:512px;display:flex;gap:6px}
.dots i{width:10px;height:10px;border-radius:50%;background:#ccc;display:block}
.dots i:first-child{background:var(--green)}
.feature{left:840px;top:186px;width:285px;height:316px;border:4px solid var(--green);border-radius:8px;background:var(--white);padding:10px}
.feature .art{height:220px;border-radius:6px;background:radial-gradient(circle at 50% 45%,#fff6c8,#9fd36a 70%,#5aa62c)}
.feature .go{margin:16px auto 0;width:200px;height:36px;border-radius:18px;background:var(--green);color:var(--white);font-weight:700;font-size:14px;display:flex;align-items:center;justify-content:center}

.sec-title{display:flex;align-items:flex-end;gap:8px;font-weight:700;color:var(--green-dark)}
.sec-title .dot{width:20px;height:20px;border-radius:50%;background:var(--green);align-self:center}
.sec-title small{font-size:11px;font-weight:500;color:var(--muted)}
.sec-title b{font-size:20px;color:var(--green)}

.genre-title{left:80px;top:556px}
.genres{left:80px;top:596px;width:740px;display:flex;gap:8px}
.genre{flex:1;height:82px;border-radius:6px;background:var(--leaf);color:var(--white);font-weight:700;font-size:12px;display:flex;flex-direction:column;align-items:center;justify-content:center;gap:8px;box-shadow:0 3px 0 var(--green-dark);white-space:nowrap}
.genre svg{width:28px;height:28px}

.sight-title{left:80px;top:732px;width:740px;padding-bottom:8px;border-bottom:2px dotted var(--green-light)}
.sight-title b{color:var(--orange)}
.cards{left:80px;top:778px;width:740px;display:grid;grid-template-columns:1fr 1fr;gap:16px 20px}
.card{height:110px;border:1px solid var(--line);padding:10px;display:flex;gap:12px;position:relative}
.card .thumb{width:110px;height:88px;background:var(--placeholder);flex:none}
.card time{font-size:11px;color:var(--muted)}
.card h3{font-size:13px;color:var(--green-dark);margin:2px 0 4px}
.card p{font-size:11px;line-height:1.5;color:var(--text)}
.card .more{position:absolute;right:10px;bottom:8px;font-size:11px;color:var(--orange)}
.list-btn{height:30px;width:120px;border-radius:4px;background:var(--green);color:var(--white);font-size:12px;font-weight:700;display:flex;align-items:center;justify-content:center}

.route-banner{left:80px;top:1214px;width:740px;height:180px;border-radius:6px;background:linear-gradient(100deg,#fbe9b8,#f7d36b 45%,#cfe7a2)}

/* sidebar */
.events{left:840px;top:546px;width:285px;height:820px;border:1px solid var(--line)}
.events h2{height:40px;background:var(--green);color:var(--white);font-size:14px;font-weight:700;display:flex;align-items:center;padding-left:14px;gap:8px}
.events h2 i{width:14px;height:14px;border-radius:50%;background:var(--white)}
.event{display:flex;gap:10px;padding:14px 12px;border-bottom:1px dotted var(--line)}
.event .thumb{width:60px;height:52px;background:var(--placeholder);flex:none}
.event p{font-size:11px;line-height:1.55}
.tweets{left:840px;top:1396px;width:285px;height:110px;border:1px solid var(--line);display:flex;flex-direction:column;align-items:center;justify-content:center;font-size:12px;color:var(--muted);line-height:1.6}
.tweets b{font-size:16px;color:var(--text)}

/* topics tabs */
.tabs{left:80px;top:1512px;width:740px;display:flex;border-bottom:3px solid var(--orange)}
.tab{flex:1;height:36px;display:flex;align-items:center;justify-content:center;font-size:12px;background:#f3f3f3;border:1px solid var(--line);border-bottom:none}
.tab.on{background:var(--orange);color:var(--white);font-weight:700;border-color:var(--orange)}
.topics{left:80px;top:1560px;width:740px;list-style:none}
.topics li{height:36px;border-bottom:1px dotted var(--line);display:flex;align-items:center;gap:16px;font-size:12px;padding-left:8px}
.topics time{color:var(--muted)}
.new{background:var(--red);color:var(--white);font-size:10px;font-weight:700;padding:1px 6px;border-radius:3px}

.concern-title{left:840px;top:1530px}
.c-banner{left:840px;width:285px;border-radius:4px}
.c-navi{top:1572px;height:62px;background:var(--leaf);color:var(--white);font-weight:700;font-size:18px;display:flex;align-items:center;justify-content:center}
.c-contest{top:1646px;height:70px;background:linear-gradient(90deg,#fff3c2,#f6c94c)}
.c-nation{top:1728px;height:70px;background:linear-gradient(90deg,#d6efc0,#8cc94e)}
.c-gray{top:1810px;height:90px;background:var(--placeholder)}

.fan-banner{left:80px;top:1820px;width:470px;height:100px;border-radius:6px;background:linear-gradient(90deg,#fff1d0,#ffd88c);border:2px solid var(--orange);padding:14px 20px}
.fan-banner b{font-size:22px;color:var(--orange)}
.fan-banner p{font-size:12px;margin-top:6px;color:var(--red)}
.info-banner{left:560px;top:1820px;width:150px;height:100px;border:2px solid var(--green-light);border-radius:6px;padding:10px;font-size:11px;line-height:1.6}
.info-banner b{color:var(--green-dark);font-size:13px}
.pic-banner{left:720px;top:1820px;width:100px;height:100px;border-radius:6px;background:linear-gradient(#cfe7f5,#8fc6e3)}

.fan-box{left:80px;top:1962px;width:1045px;height:306px;border:1px solid var(--line);display:flex;align-items:center;justify-content:center;font-size:13px;color:var(--muted)}
.to-top{left:1064px;top:2300px;font-size:11px;color:var(--muted)}

/* footer */
.footer{left:0;top:2322px;width:1200px;height:148px;background:var(--green-pale);border-top:3px solid var(--green)}
.sitemap{left:80px;top:2338px;width:820px;font-size:11px;line-height:2;color:var(--text)}
.sitemap b{color:var(--green-dark)}
.scout{left:924px;top:2340px;width:200px;height:116px;background:var(--white);border:1px solid var(--line);display:flex;align-items:center;justify-content:center;font-size:12px;color:var(--muted)}
.copy{left:0;top:2470px;width:1200px;height:22px;background:var(--green-dark);color:var(--white);font-size:10px;display:flex;align-items:center;padding-left:80px}
</style>
</head>
<body>
<div class="abs sky"></div>
<div class="abs cloud" style="left:380px;top:70px;width:180px;height:50px"></div>
<div class="abs cloud" style="left:900px;top:40px;width:140px;height:40px"></div>
<div class="abs cloud" style="left:40px;top:150px;width:220px;height:50px"></div>

<nav class="abs utility"><a>観光情報</a>|<a>マップ</a>|<a>お問い合わせ</a>|<a>サイトマップ</a></nav>

<p class="abs tagline">あおば情報ならほぼおまかせ！ 地域情報ポータルサイト</p>
<a class="abs site-name"><span class="mark"></span><strong>さとやま便</strong></a>
<p class="abs site-sub">Satoyama Line</p>

<div class="abs font-size">文字サイズ <span class="btn on">大</span><span class="btn">中</span><span class="btn">小</span></div>
<div class="abs post-buttons">
  <a class="post-btn"><i></i>トピックス投稿</a>
  <a class="post-btn"><i></i>イベント投稿</a>
  <a class="post-btn"><i></i>わいわい広場投稿</a>
</div>

<div class="abs sheet"></div>
<div class="abs slider" role="img" aria-label="スライドショーの写真"></div>
<div class="abs dots"><i></i><i></i><i></i><i></i><i></i></div>
<div class="abs feature">
  <div class="art" role="img" aria-label="2014年の地域イベントのバナー"></div>
  <a class="go">詳しくはこちら ▶</a>
</div>

<h2 class="abs sec-title genre-title"><span class="dot"></span><small>ジャンルから</small><b>探す</b></h2>
<div class="abs genres">
  <a class="genre"><svg viewBox="0 0 24 24"><rect x="3" y="5" width="18" height="16" rx="2" fill="#fff"/></svg>イベント</a>
  <a class="genre"><svg viewBox="0 0 24 24"><path d="M12 2a7 7 0 0 0-7 7c0 5 7 13 7 13s7-8 7-13a7 7 0 0 0-7-7z" fill="#fff"/></svg>観光ナビ</a>
  <a class="genre"><svg viewBox="0 0 24 24"><path d="M12 2l3 7h7l-6 4 2 8-6-5-6 5 2-8-6-4h7z" fill="#fff"/></svg>みちしるべ</a>
  <a class="genre"><svg viewBox="0 0 24 24"><rect x="4" y="3" width="16" height="18" rx="1" fill="#fff"/></svg>ライブラリー</a>
  <a class="genre"><svg viewBox="0 0 24 24"><path d="M4 20l2-6 10-10 4 4-10 10z" fill="#fff"/></svg>ブログ</a>
  <a class="genre"><svg viewBox="0 0 24 24"><circle cx="12" cy="12" r="9" fill="none" stroke="#fff" stroke-width="3"/></svg>リンク</a>
</div>

<h2 class="abs sec-title sight-title"><span class="dot"></span><small>ふるさと特派員がお送りする</small><b>観光情報</b></h2>
<div class="abs cards">
  <article class="card"><div class="thumb" role="img" aria-label="観光スポットの写真"></div><div><time>12/04</time><h3>冬のにおいを感じさせる「天蓋」</h3><p>紅葉の季節が終わると、山あいの里はいよいよ冬の支度を始めます。</p></div><a class="more">▶ もっと見る</a></article>
  <article class="card"><div class="thumb" role="img" aria-label="観光スポットの写真"></div><div><time>12/04</time><h3>冬のにおいを感じさせる「天蓋」</h3><p>紅葉の季節が終わると、山あいの里はいよいよ冬の支度を始めます。</p></div><a class="more">▶ もっと見る</a></article>
  <article class="card"><div class="thumb" role="img" aria-label="観光スポットの写真"></div><div><time>12/04</time><h3>冬のにおいを感じさせる「天蓋」</h3><p>紅葉の季節が終わると、山あいの里はいよいよ冬の支度を始めます。</p></div><a class="more">▶ もっと見る</a></article>
  <article class="card"><div class="thumb" role="img" aria-label="観光スポットの写真"></div><div><time>12/04</time><h3>冬のにおいを感じさせる「天蓋」</h3><p>紅葉の季節が終わると、山あいの里はいよいよ冬の支度を始めます。</p></div><a class="more">▶ もっと見る</a></article>
  <article class="card"><div class="thumb" role="img" aria-label="観光スポットの写真"></div><div><time>12/04</time><h3>冬のにおいを感じさせる「天蓋」</h3><p>紅葉の季節が終わると、山あいの里はいよいよ冬の支度を始めます。</p></div><a class="more">▶ もっと見る</a></article>
  <article class="card"><div class="thumb" role="img" aria-label="観光スポットの写真"></div><div><time>12/04</time><h3>冬のにおいを感じさせる「天蓋」</h3><p>紅葉の季節が終わると、山あいの里はいよいよ冬の支度を始めます。</p></div><a class="more">▶ もっと見る</a></article>
</div>
<a class="abs list-btn" style="left:700px;top:1156px">一覧を見る ▶</a>

<div class="abs route-banner" role="img" aria-label="若竹市のおすすめベスト観光ルートのイラストバナー"></div>

<aside class="abs events">
  <h2><i></i>今日から1週間のイベント</h2>
  <div class="event"><div class="thumb"></div><p>12/04 〜 12/10<br>冬の里山あかり展。駅前広場にて開催、入場無料です。</p></div>
  <div class="event"><div class="thumb"></div><p>12/05 〜 12/07<br>かに祭り。港の朝市で旬の味覚をお楽しみください。</p></div>
  <div class="event"><div class="thumb"></div><p>12/06<br>そば打ち体験教室。道具は会場でご用意しています。</p></div>
  <div class="event"><div class="thumb"></div><p>12/07<br>冬の星空観察会。防寒着をお持ちのうえご参加ください。</p></div>
  <div class="event"><div class="thumb"></div><p>12/08<br>城下町クリスマス市。手作り雑貨の店が並びます。</p></div>
  <div class="event"><div class="thumb"></div><p>12/09<br>温泉街ライトアップ。夕暮れから夜まで点灯します。</p></div>
  <div class="event"><div class="thumb"></div><p>12/10<br>地元の音楽会。公民館ホールにて午後二時開演。</p></div>
  <div class="event"><div class="thumb"></div><p>12/10<br>朝市の日。新鮮な野菜と加工品を販売します。</p></div>
  <div class="event"><div class="thumb"></div><p>12/10<br>親子の木工教室。参加は事前申込が必要です。</p></div>
</aside>
<div class="abs tweets">ツイッター<b>Tweets</b>コンテンツ</div>

<div class="abs tabs"><a class="tab on">トピックス</a><a class="tab">しけん</a><a class="tab">青葉暮らし</a><a class="tab">青葉グルメ</a><a class="tab">ヘッドライン</a><a class="tab">観光情報</a></div>
<ul class="abs topics">
  <li><time>12/04</time>よくある質問ページのご案内<span class="new">NEW</span></li>
  <li><time>12/04</time>「さとやま便投稿者」投稿者限定の募集について<span class="new">NEW</span></li>
  <li><time>12/04</time>年末年始の掲載スケジュールについて</li>
  <li><time>12/04</time>地域情報誌の発行のお知らせ</li>
  <li><time>12/04</time>冬の写真コンテスト作品の募集について</li>
</ul>
<a class="abs list-btn" style="left:700px;top:1762px">一覧を見る ▶</a>

<h2 class="abs sec-title concern-title"><span class="dot"></span><small>気になる</small><b>コンテンツ</b></h2>
<a class="abs c-banner c-navi">あおば☆みちしるべ</a>
<div class="abs c-banner c-contest" role="img" aria-label="写真コンテストのバナー"></div>
<div class="abs c-banner c-nation" role="img" aria-label="地域を全国へ発信するバナー"></div>
<div class="abs c-banner c-gray" role="img" aria-label="広告バナー"></div>

<div class="abs fan-banner"><b>青葉ファンクラブ</b><p>青葉でおトクにおもてなし！ スタンプラリーを実施中</p></div>
<div class="abs info-banner"><b>地元の業者情報</b><br>地元のお店や事業者を探せます。</div>
<div class="abs pic-banner" role="img" aria-label="風景写真のバナー"></div>

<div class="abs fan-box">地域情報を共に発信（青葉ファンクラブ）</div>
<a class="abs to-top">▲ Top page</a>

<footer class="abs footer"></footer>
<div class="abs sitemap">
  <b>【総合カテゴリ】</b><br>
  観光 | 自然 | 歴史 | 文化 | グルメ | 温泉 | 体験 | 宿泊 | 交通 | 買い物 | 特産品 | 暮らし | 子育て | 医療 | 教育<br>
  このサイトについて | プライバシーポリシー | 利用規約 | リンク集 | 投稿について | お問い合わせ<br>
  運営：地域振興の会 事務局 | 受付時間 平日 9:00〜17:00
</div>
<div class="abs scout">スカウト情報</div>
<div class="abs copy">Copyright © Satoyama Line. All Rights Reserved.</div>
</body>
</html>
```